New IPv6 service needs a Web Design

We're launching a brand new service which is designed to connect the current Internet Protocol (IPv4) to the new Internet Protocol (IPv6).
The logo can be found at http://www.brelvo-link.example
We're looking for a clean and simple design, nothing super-fancy. There has to be room for some menu items and a place where people can login (so an e-mail and password box and login button, which must be replaced by the username and a logout button when the user is logged in).
We need a place for a rotating billboard (see http://qa.zx for an example) or a video.
Designs that incorporate IPv4 - IPv6 elements (images with interconnecting networks, videos doing the same) will be rated higher, although the basic design is still the primary concern.
We need :
- A main page, with the rotating billboard and some other typical main page stuff
- 2 subpages with different formatted content blocks (1 column and 2 column)
This is a very short design contest, since we intend to go live very soon. Decision will be made quickly.
PSD file is sufficient, but it must be easy to slice to HTML/CSS (but we'll do that part ourselves).
Target Market(s)
IT Professionals
Industry/Entity Type
Internet
Look and feel
Each slider illustrates characteristics of the customer's brand and the style your logo design should communicate.

```html
<!DOCTYPE html>
<html lang="en">
<head>
<meta charset="utf-8">
<title>Brelvo – IPv6 Service</title>
<link href="https://fonts.googleapis.com/css2?family=Arimo:wght@400;700&display=swap" rel="stylesheet">
<style>
:root{
  --blue:#0d5c99;
  --blue-bright:#1a6fb3;
  --red:#d9202c;
  --ink:#222;
  --muted:#555;
  --footer:#e3e3e3;
  --btn-dark:#3a3a3a;
}
*{margin:0;padding:0;box-sizing:border-box}
html,body{width:1200px;height:1181px;overflow:hidden}
body{font-family:"Arimo",Arial,sans-serif;color:var(--ink);background:#fff;position:relative}
.page{position:relative;width:1200px;height:1181px;background:linear-gradient(#e9f1f8 0,#fff 160px)}
.abs{position:absolute}
.topbar{left:0;top:0;width:1200px;height:7px;background:var(--blue)}
.login{left:920px;top:7px;width:83px;height:21px;background:var(--blue-bright);border-radius:0 0 5px 5px;color:#fff;font-size:11px;display:flex;align-items:center;justify-content:center;gap:6px;text-decoration:none}
.brand{display:flex;align-items:center;gap:8px;font-weight:700;color:var(--blue);letter-spacing:-1px}
.brand .dot{width:22px;height:22px;border-radius:50%;background:var(--red)}
.brand-head{left:213px;top:50px;font-size:52px}
.main-nav{left:556px;top:81px;display:flex;font-size:12.5px}
.main-nav a{position:absolute;white-space:nowrap;text-decoration:none;color:var(--blue)}
.main-nav a.current{color:var(--ink)}
.hero-title{left:212px;top:178px;font-size:26px;line-height:26.5px;width:320px;color:var(--ink)}
.b{color:var(--blue)}.r{color:var(--red)}
.btn{display:flex;align-items:center;gap:12px;border-radius:8px;background:linear-gradient(#5b5b5b,#2e2e2e);color:#fff;font-size:16px;font-weight:700;text-decoration:none;padding-left:11px;box-shadow:0 2px 3px rgba(0,0,0,.35);letter-spacing:-.3px}
.btn .ico{width:24px;height:24px;border:2px solid #fff;border-radius:50%;display:flex;align-items:center;justify-content:center}
.hero-btn{left:213px;top:313px;width:152px;height:41px}
.hint{font-size:9px;line-height:12px;color:#444}
.hero-hint{left:382px;top:322px}
.hero-visual{left:538px;top:137px;width:465px;height:302px;background:radial-gradient(circle at 75% 35%,#e7c3a6 0 12%,transparent 13%),radial-gradient(ellipse at 78% 85%,#a9c8e6 0 30%,transparent 31%),linear-gradient(135deg,#f4f8fc,#d5e5f4)}
.slider-ctrl{left:894px;top:410px;display:flex;align-items:center;gap:5px}
.slider-ctrl i{display:block;width:7px;height:7px;background:#222}
.benefits-band{left:205px;top:438px;width:798px;height:16px;background:radial-gradient(ellipse at 50% 0,rgba(0,0,0,.12),transparent 70%)}
.benefits-tab{left:517px;top:439px;width:164px;height:24px;background:var(--blue);clip-path:polygon(0 0,100% 0,92% 100%,8% 100%);border-radius:0 0 10px 10px;color:#fff;font-size:11.5px;font-weight:700;display:flex;align-items:center;justify-content:center}
.benefit{width:140px;text-align:center;font-size:11px;line-height:15.5px;color:#333}
.benefit svg{display:block;margin:0 auto 10px}
.side-arrow{width:22px;height:36px;border-radius:50%;background:radial-gradient(#f2f2f2,#d6d6d6);display:flex;align-items:center;justify-content:center;color:#777;font-size:16px;font-weight:700}
.divider{left:210px;top:600px;width:790px;height:1px;background:#e8e8e8}
.monitor{left:210px;top:632px;width:366px;height:246px;background:#111;border-radius:8px;border:2px solid #888}
.screen{left:16px;top:15px;width:334px;height:210px;background:radial-gradient(circle at 55% 40%,#d0dbe5,#7a93a8)}
.play{left:138px;top:45px}
.controls{left:0;bottom:0;width:100%;height:17px;background:#1c1c1c}
.stand{left:345px;top:878px;width:96px;height:60px;background:linear-gradient(90deg,#bbb,#eee 50%,#bbb);clip-path:polygon(14% 0,86% 0,95% 100%,5% 100%)}
.stand-base{left:300px;top:936px;width:186px;height:10px;border-radius:50%;background:radial-gradient(rgba(0,0,0,.18),transparent 70%)}
.mon-label{left:0;top:226px;width:100%;text-align:center;color:#fff;font-size:9px;font-weight:700}
.features h2{font-size:18.5px;line-height:24px;font-weight:400;margin-bottom:22px}
.features{left:625px;top:641px;width:390px}
.features p{font-size:11px;line-height:15.5px;color:#222;margin-bottom:13px}
.more-box{left:626px;top:876px;width:284px;height:66px;background:#e3e3e3;border-radius:8px}
.more-btn{left:8px;top:12px;width:153px;height:41px}
.more-hint{left:178px;top:20px}
.footer{left:0;top:994px;width:1200px;height:187px;background:var(--footer)}
.footer::before{content:"";position:absolute;left:210px;top:0;width:780px;height:14px;background:radial-gradient(ellipse at 50% 0,rgba(0,0,0,.1),transparent 70%)}
.foot-nav a{position:absolute;top:55px;font-size:12.5px;color:#222;text-decoration:none;white-space:nowrap}
.foot-nav a.current{color:var(--red)}
.brand-foot{left:840px;top:45px;font-size:46px}
.copy{right:189px;top:117px;font-size:9.5px;color:#111}
</style>
</head>
<body>
<div class="page">
  <div class="abs topbar"></div>
  <a class="abs login" href="#">
    <svg width="9" height="10" viewBox="0 0 9 10"><rect x="0.5" y="4" width="8" height="6" rx="1" fill="#fff"/><path d="M2 4V3a2.5 2.5 0 0 1 5 0v1" stroke="#fff" fill="none"/></svg>LOGIN</a>

  <div class="abs brand brand-head"><span class="dot"></span>brelvo</div>

  <nav class="abs main-nav">
    <a class="current" style="left:0;top:0">HOME</a>
    <a style="left:67px;top:0">ABOUT IPV6</a>
    <a style="left:169px;top:0">BENEFITS</a>
    <a style="left:260px;top:0">TESTIMONIAL</a>
    <a style="left:365px;top:0">CONTACT US</a>
  </nav>

  <h1 class="abs hero-title" style="font-weight:400">IPv6 <span class="r">reduces</span> <span class="b">the size of routing tables</span> and makes routing <span class="b">more</span> <span class="r">efficient</span> <span class="b">and</span> <span class="r">hierarchical</span><span class="b">.</span></h1>

  <a class="abs btn hero-btn" href="#"><span class="ico"><svg width="10" height="12" viewBox="0 0 10 12"><path d="M5 1v8M1.5 6 5 9.5 8.5 6" stroke="#fff" stroke-width="2" fill="none"/></svg></span>Read More</a>
  <div class="abs hint hero-hint">Click here for<br>more details on IPv6</div>

  <div class="abs hero-visual" role="img" aria-label="Smiling support engineer beside a network of connected computers"></div>
  <div class="abs slider-ctrl">
    <svg width="20" height="16" viewBox="0 0 20 16"><path d="M0 8 20 0 14 8 20 16Z" fill="var(--blue)"/></svg>
    <i></i><i></i><i></i>
    <svg width="20" height="16" viewBox="0 0 20 16"><path d="M20 8 0 0 6 8 0 16Z" fill="var(--red)"/></svg>
  </div>

  <div class="abs benefits-band"></div>
  <div class="abs benefits-tab">IPv6 BENEFITS</div>

  <div class="abs side-arrow" style="left:208px;top:506px">‹</div>
  <div class="abs side-arrow" style="left:976px;top:506px">›</div>

  <div class="abs benefit" style="left:250px;top:484px">
    <svg width="58" height="36" viewBox="0 0 58 36"><rect x="22" y="0" width="14" height="10" fill="var(--blue)"/><path d="M29 10v10M9 20V15h40v5" stroke="var(--blue)" stroke-width="3" fill="none"/><rect x="1" y="24" width="16" height="10" fill="var(--red)"/><rect x="21" y="24" width="16" height="10" fill="var(--red)"/><rect x="41" y="24" width="16" height="10" fill="var(--red)"/></svg>
    Efficient<br>Routing</div>
  <div class="abs benefit" style="left:391px;top:484px">
    <svg width="44" height="38" viewBox="0 0 44 38"><path d="M22 0 36 14H28V26H16V14H8Z" fill="var(--blue)"/><path d="M2 22v10h40V22" stroke="var(--red)" stroke-width="6" fill="none"/></svg>
    Efficient<br>Packet Processing</div>
  <div class="abs benefit" style="left:537px;top:482px">
    <svg width="50" height="50" viewBox="0 0 50 50"><path d="M25 4A21 21 0 0 0 25 46" stroke="var(--red)" stroke-width="7" fill="none"/><path d="M25 46A21 21 0 0 0 25 4" stroke="var(--blue)" stroke-width="7" fill="none" stroke-dasharray="40 60"/><path d="M22 -1 31 5 22 10Z" fill="var(--red)"/></svg>
    Directed<br>Data Flows</div>
  <div class="abs benefit" style="left:680px;top:483px">
    <svg width="52" height="48" viewBox="0 0 52 48"><rect x="2" y="2" width="48" height="34" fill="none" stroke="var(--blue)" stroke-width="4"/><path d="M18 44 26 36 34 44Z" fill="var(--red)"/><rect x="14" y="43" width="24" height="3" fill="var(--red)"/></svg>
    Simplified Network<br>Configuration</div>
  <div class="abs benefit" style="left:824px;top:486px">
    <svg width="50" height="44" viewBox="0 0 50 44"><circle cx="20" cy="6" r="6" fill="var(--red)"/><circle cx="12" cy="14" r="6" fill="var(--blue)"/><path d="M2 40c0-14 4-20 10-20s10 6 10 20Z" fill="var(--blue)"/><path d="M18 30c2-10 4-14 8-14" stroke="var(--red)" stroke-width="5" fill="none"/><path d="M26 30l7 7 14-14" stroke="var(--blue)" stroke-width="5" fill="none"/></svg>
    Support For<br>New Services</div>

  <div class="abs divider"></div>

  <div class="abs monitor">
    <div class="abs screen" role="img" aria-label="Video still of a world map over a networked background">
      <svg class="abs play" width="62" height="62" viewBox="0 0 62 62"><circle cx="31" cy="31" r="29" fill="rgba(255,255,255,.15)" stroke="#fff" stroke-width="3"/><path d="M24 18 45 31 24 44Z" fill="#fff"/></svg>
      <div class="abs controls">
        <svg width="334" height="17" viewBox="0 0 334 17"><rect x="8" y="3" width="14" height="11" fill="#1d8ad0"/><path d="M13 6 18 8.5 13 11Z" fill="#fff"/><rect x="32" y="7" width="146" height="3" fill="#444"/><rect x="32" y="7" width="70" height="3" fill="#1d8ad0"/><rect x="332" y="7" width="0" height="0"/><rect x="300" y="6" width="14" height="5" fill="#1d8ad0"/></svg>
      </div>
    </div>
    <div class="abs mon-label">brelvo</div>
  </div>
  <div class="abs stand"></div>
  <div class="abs stand-base"></div>

  <section class="abs features">
    <h2><span class="r">IPv6</span> Also Implements <span class="b">Additional Features</span> Not Present in <span class="r">IPv4,</span> Feel The Differences</h2>
    <p>It simplifies aspects of address assignment , network renumbering and router announcements when changing network connectivity providers.</p>
    <p>The Internet operates by transferring data between hosts in packets that are routed across networks as specified by routing protocols.</p>
    <p>These packets require an addressing scheme, such as IPv4 or IPv6, to specify their source and destination addresses. Each host, computer or other device on the Internet requires an IP address in order to communicate.</p>
  </section>

  <div class="abs more-box">
    <a class="abs btn more-btn" href="#"><span class="ico"><svg width="10" height="12" viewBox="0 0 10 12"><path d="M5 1v8M1.5 6 5 9.5 8.5 6" stroke="#fff" stroke-width="2" fill="none"/></svg></span>Read More</a>
    <div class="abs hint more-hint">Click here for<br>more details on IPv6</div>
  </div>

  <footer class="abs footer">
    <nav class="foot-nav">
      <a class="current" style="left:227px">HOME</a>
      <a style="left:294px">ABOUT IPV6</a>
      <a style="left:396px">BENEFITS</a>
      <a style="left:487px">TESTIMONIAL</a>
      <a style="left:592px">CONTACT US</a>
    </nav>
    <div class="abs brand brand-foot"><span class="dot"></span>brelvo</div>
    <div class="abs copy">Copyright ©2012 Brelvo, All Right Reserved</div>
  </footer>
</div>
</body>
</html>
```